Create a Graphic About YOURSELF and PixelHarbor

PixelHarbor would like you (designers) to create an awesome graphic to promote YOURSELF and your profile on PixelHarbor!

Your graphic should communicate your name, your services and should mention PixelHarbor.

The design should be perfect for sharing on Chatterly. Here's an example of what we'd like http://blog.pixelharbor-example.ca/article/333/pixelharbor-launches-3000-hire-me-social-design-contest

Once you submitted your design, we'd love you to share the design ('advertisement') and promote yourself and PixelHarbor to your friends and potential customers. So make your submissions great and get your friends to vote for your design by 'Liking' it on Chatterly!

Prizes:
$1500 - "PixelHarbor Community" prize awarded to the designer with the most Chatterly 'Likes'
5 x $50 for the next 5 'most liked' designs on Chatterly

$1000 - "Hire Me" prize awarded to the designer who receives the most client invites
5 x $50 for the next 5 'most invited' designers

In summary, this is a great opportunity for you to increase your exposure to PixelHarbor customers and win cash prizes. Show off your design skills and get hired by PixelHarbor customers from around the world!

Target Market(s)

Fans, friends and customers of YOU

Industry/Entity Type

Cash

Requirements
Must have
• 1) Include your PixelHarbor user name on the graphic so customers can find you in the PixelHarbor Designer Directory
2) Include the tagline "Hire Me on PixelHarbor.com!" in your graphic design.
3) Share your design's URL on our Chatterly wall at http://chatterly-example.com/pixelharbor and get your friends to 'like' your design.
Nice to have
• 1) Include a tagline that expresses your design approach/philosophy
2) Artwork dimensions: 403 x 403 px
3) You can submit more than 1 design!
Should not have
• You must own the copyright of any images you use including stock imagery.

```html
<!DOCTYPE html>
<html lang="en">
<head>
<meta charset="utf-8">
<title>Brightframe Designs – Services</title>
<link rel="stylesheet" href="https://fonts.googleapis.com/css2?family=Josefin+Sans:wght@300;400&display=swap">
<style>
  :root {
    --ink-black: #141414;
    --band-dark: #262626;
    --band-mid: #3a3a3a;
    --paper: #f4f4f4;
    --paper-shade: #dedede;
    --text-dark: #2e2e2e;
    --text-light: #f2f2f2;
    --text-muted: #bdbdbd;
    --ring-white: #ffffff;
    --icon-tone-a: #e9e9e9;
    --icon-tone-b: #bdbdbd;
    --stem: #555555;
  }
  * { margin: 0; padding: 0; box-sizing: border-box; }
  html, body { width: 1200px; height: 646px; overflow: hidden; background: var(--paper); }
  body { font-family: "Josefin Sans", "Century Gothic", sans-serif; font-weight: 300; }

  .card { position: relative; width: 1200px; height: 646px; overflow: hidden;
    background: linear-gradient(180deg, var(--paper-shade) 0%, var(--paper) 45%, #ffffff 100%); }

  .header-band { position: absolute; left: 0; top: 0; width: 1200px; height: 172px;
    background: linear-gradient(180deg, var(--ink-black) 0%, var(--band-dark) 55%, var(--band-mid) 100%);
    border-bottom: 2px solid #555; }
  .header-band::after { content: ""; position: absolute; left: 0; right: 0; top: 98px; height: 74px;
    background: linear-gradient(180deg, rgba(255,255,255,0.05), rgba(255,255,255,0.12)); }

  .studio-name { position: absolute; top: 18px; left: 0; width: 1200px; text-align: center;
    color: var(--text-light); font-size: 31px; font-weight: 400; letter-spacing: 3px; white-space: nowrap; }
  .studio-rule { position: absolute; top: 62px; left: 332px; width: 536px; height: 1px;
    background: rgba(255,255,255,0.55); }
  .studio-tagline { position: absolute; top: 71px; left: 0; width: 1200px; text-align: center;
    color: var(--text-muted); font-size: 15px; font-weight: 400; letter-spacing: 1px; white-space: nowrap; }

  .service { position: absolute; top: 82px; width: 400px; text-align: center; color: var(--text-dark); }
  .service--design { left: -15px; }
  .service--seo { left: 396px; }
  .service--dev { left: 806px; }

  .service-badge { display: block; margin: 0 auto; width: 206px; height: 206px; }
  .service-stem { width: 2px; height: 26px; margin: 0 auto; background: var(--stem); }
  .service-dot { width: 8px; height: 8px; border-radius: 50%; background: var(--stem); margin: 3px auto 0; }

  .service-title { margin-top: 14px; font-size: 27px; font-weight: 300; letter-spacing: 0.5px;
    text-transform: uppercase; white-space: nowrap; }
  .service-text { margin: 8px auto 0; width: 322px; font-size: 19.5px; line-height: 24px; }

  .contact-band { position: absolute; left: 0; top: 541px; width: 1200px; height: 105px;
    background: linear-gradient(180deg, #1d1d1d, var(--ink-black)); border-top: 2px solid #4a4a4a; }
  .contact-title { position: absolute; left: 37px; top: 36px; color: var(--text-light);
    font-size: 33px; font-weight: 300; white-space: nowrap; }
  .contact-bracket { position: absolute; left: 480px; top: 27px; width: 56px; height: 50px; }
  .contact-list { position: absolute; left: 548px; top: 43px; display: flex; gap: 16px;
    color: var(--text-light); font-size: 20px; font-weight: 400; list-style: none; white-space: nowrap; }
</style>
</head>
<body>
<main class="card">
  <header class="header-band">
    <h1 class="studio-name">BRIGHTFRAME DESIGNS</h1>
    <div class="studio-rule"></div>
    <p class="studio-tagline">Hire Me on PixelHarbor.com! &nbsp;·&nbsp; PixelHarbor user: brightframe</p>
  </header>

  <section class="service service--design">
    <svg class="service-badge" viewBox="0 0 206 206" role="img" aria-label="Paintbrush illustration for web design">
      <defs>
        <radialGradient id="badgeFillA" cx="50%" cy="40%" r="60%">
          <stop offset="0" stop-color="#e9e9e9"/><stop offset="1" stop-color="#bdbdbd"/>
        </radialGradient>
      </defs>
      <circle cx="103" cy="103" r="100" fill="#ffffff" stroke="#cfcfcf" stroke-width="2"/>
      <circle cx="103" cy="103" r="84" fill="url(#badgeFillA)"/>
    </svg>
    <div class="service-stem"></div>
    <div class="service-dot"></div>
    <h2 class="service-title">Web Design</h2>
    <p class="service-text">I offer high quality minimal web design services at an affordable price. I will also match the price that any other web designer charges.</p>
  </section>

  <section class="service service--seo">
    <svg class="service-badge" viewBox="0 0 206 206" role="img" aria-label="T-square illustration for SEO services">
      <defs>
        <radialGradient id="badgeFillB" cx="50%" cy="40%" r="60%">
          <stop offset="0" stop-color="#e9e9e9"/><stop offset="1" stop-color="#bdbdbd"/>
        </radialGradient>
      </defs>
      <circle cx="103" cy="103" r="100" fill="#ffffff" stroke="#cfcfcf" stroke-width="2"/>
      <circle cx="103" cy="103" r="84" fill="url(#badgeFillB)"/>
    </svg>
    <div class="service-stem"></div>
    <div class="service-dot"></div>
    <h2 class="service-title">SEO Services</h2>
    <p class="service-text">My SEO services are of the highest caliber and will always meet todays web coding standards. From link building, to back linking. I cover it all!</p>
  </section>

  <section class="service service--dev">
    <svg class="service-badge" viewBox="0 0 206 206" role="img" aria-label="Notepad and pencil illustration for development">
      <defs>
        <radialGradient id="badgeFillC" cx="50%" cy="40%" r="60%">
          <stop offset="0" stop-color="#e9e9e9"/><stop offset="1" stop-color="#bdbdbd"/>
        </radialGradient>
      </defs>
      <circle cx="103" cy="103" r="100" fill="#ffffff" stroke="#cfcfcf" stroke-width="2"/>
      <circle cx="103" cy="103" r="84" fill="url(#badgeFillC)"/>
    </svg>
    <div class="service-stem"></div>
    <div class="service-dot"></div>
    <h2 class="service-title">Development</h2>
    <p class="service-text">I code using up-to-date web-standards. All of my code is clean, efficient, and cross-browser friendly! Java, CSS, HTML, HTML5, Flash; you name it, I can do it.</p>
  </section>

  <footer class="contact-band">
    <h2 class="contact-title">CONTACT INFORMATION</h2>
    <svg class="contact-bracket" viewBox="0 0 56 50" aria-hidden="true">
      <path d="M0 25 H30 M56 2 H30 V48 H56" fill="none" stroke="#bbbbbb" stroke-width="1.5"/>
    </svg>
    <ul class="contact-list">
      <li class="contact-phone">555.014.2387</li>
      <li class="contact-email">brightframe@example.com</li>
      <li class="contact-social">Chatterly.com/bfd89</li>
    </ul>
  </footer>
</main>
</body>
</html>
```